Brisk Hollow Builders Needs A Flyer

We need a flyer for our newest product "The Cedarlane Garden Workroom"

Here is some copy for the flyer:

1. More and more people everyday are working from home and finding it difficult to disconnect from home activities in order to focus on their work. They are also finding it very expensive to add on to their existing house for a quiet place. Our archatectually stunning, Cedarlane Garden Workroom is the answer. The office studio measures 16' wide and 10' deep. 160 Square feet of space.

Perfect for dozens of purposes. Home office, design studio, artist studio, home school office, reading room, craft studio, drafting room.

Features include:

- Steel Framing. 40-60% lighter then wood, higher strength to weight ratio, resistant to mold and fire and steel is the most recycled material on earth!
- Spray foam insulation. Cool in the summer and warm in the winter.
- HVAC Mini Split with wireless remote control and thermostat.
- 100% Off grid with enough solar and battery storage to run your entire office. No need to pay for an expensive electric installation.
- Flush fitting floor outlets to reduce wires.
- TV mount (Optional with pre-wired electric, HDMI, digital audio & Cat 6)
- Windows are tempered glass custom made by Morvik Glazing.
- Solar qualifies for a 26% tax credit. This is not a write-off rather it is a direct reduction on your tax obligation.
- Thousands of dollars less than adding onto your home.
- Custom color, siding, features available.

This beautiful back yard office is delivered 100% assembled and ready to enjoy on the day of delivery.

We ship nationwide from our factory in South Carolina. Give us a call anytime to speak to a designer and start your dream office today!

555-318-4027
info@BriskHollowBuilders.example

```html
<!DOCTYPE html>
<html lang="en">
<head>
<meta charset="utf-8">
<title>Brisk Hollow Builders — Cedarlane Garden Workroom Flyer</title>
<link rel="stylesheet" href="https://fonts.googleapis.com/css2?family=Bebas+Neue&family=Montserrat:wght@400;500;700;800;900&display=swap">
<style>
  :root {
    --green-dark: #0b4a12;
    --green-badge: #0f5a14;
    --amber: #fbbf0b;
    --orange: #f7960c;
    --ink: #1f1f1f;
    --grey-text: #666666;
    --white: #ffffff;
    --sky: #8ec0ec;
    --sky-light: #d6e6f4;
    --foliage: #6f8f56;
    --charcoal: #3b3d3b;
  }
  * { margin: 0; padding: 0; box-sizing: border-box; }
  html, body { width: 874px; height: 1200px; overflow: hidden; background: var(--white); }
  body { font-family: "Montserrat", sans-serif; color: var(--ink); }

  .flyer { position: relative; width: 874px; height: 1200px; overflow: hidden; background: var(--white); }

  .hero-photo {
    position: absolute; left: 0; top: 0; width: 874px; height: 640px;
    background:
      radial-gradient(ellipse 260px 150px at 440px 400px, rgba(236, 226, 208, 0.85), rgba(236, 226, 208, 0) 100%),
      radial-gradient(ellipse 380px 230px at 450px 380px, rgba(59, 61, 59, 0.9), rgba(59, 61, 59, 0) 100%),
      radial-gradient(ellipse 160px 260px at 820px 120px, rgba(86, 120, 60, 0.8), rgba(86, 120, 60, 0) 100%),
      linear-gradient(180deg, var(--sky) 0%, var(--sky-light) 26%, var(--foliage) 50%, #55704a 75%, #9aa985 100%);
  }

  .shapes { position: absolute; left: 0; top: 0; width: 874px; height: 1200px; }

  .brand-disc {
    position: absolute; left: -24px; top: -40px; width: 320px; height: 275px;
    border-radius: 50%; background: rgba(240, 240, 240, 0.9);
  }
  .brand-mark {
    position: absolute; left: 124px; top: 78px; width: 28px; height: 28px;
    border-radius: 50%; background: var(--orange);
  }
  .brand-name {
    position: absolute; left: 38px; top: 118px; width: 200px;
    font-weight: 800; font-size: 20px; line-height: 22px; color: var(--green-dark);
    text-align: center;
  }

  .uses-card {
    position: absolute; left: 56px; top: 441px; width: 182px; height: 178px;
    border-radius: 12px; padding: 9px 0 0 14px;
    background: linear-gradient(180deg, var(--amber), var(--orange));
  }
  .uses-card h3 { font-weight: 800; font-size: 14.5px; letter-spacing: 0.3px; margin-bottom: 1px; }
  .uses-card ul { list-style: none; }
  .uses-card li { font-weight: 700; font-size: 12.3px; line-height: 17px; padding-left: 4px; }
  .uses-card li::before { content: "• "; font-size: 9px; }

  .delivery-badge {
    position: absolute; left: 667px; top: 430px; width: 162px; height: 216px;
    background: var(--orange); border-radius: 0 0 81px 81px; padding: 5px;
  }
  .delivery-badge .inner {
    width: 100%; height: 100%; background: var(--green-badge);
    border-radius: 0 0 76px 76px; color: var(--white); text-align: center;
    font-weight: 900; padding-top: 22px;
  }
  .delivery-badge .lead { font-size: 20px; line-height: 24px; }
  .delivery-badge .big { font-size: 46px; line-height: 52px; letter-spacing: -1px; }
  .delivery-badge .rest { font-size: 17.5px; line-height: 22px; margin-top: 4px; }

  .headline { position: absolute; left: 70px; top: 640px; font-weight: normal; }
  .headline .kicker { display: block; font-weight: 900; font-size: 23px; line-height: 28px; letter-spacing: 0.2px; }
  .headline .title {
    display: block; font-family: "Bebas Neue", sans-serif; color: var(--green-dark);
    font-size: 78px; line-height: 72px; margin-top: 4px;
  }

  .intro {
    position: absolute; left: 360px; top: 637px; width: 440px;
    font-size: 13.2px; line-height: 21.6px; color: var(--grey-text);
  }

  .features-card {
    position: absolute; left: 51px; top: 833px; width: 772px; height: 267px;
    border-radius: 24px; padding: 8px 0 0 21px;
    background: linear-gradient(180deg, var(--amber) 0%, #f9ad0c 60%, var(--orange) 100%);
  }
  .features-card h3 { font-weight: 800; font-size: 18px; line-height: 24px; margin-bottom: 2px; }
  .features-card ul { list-style: none; width: 700px; }
  .features-card li {
    position: relative; padding-left: 12px;
    font-size: 11.6px; line-height: 14.8px; font-weight: 500; margin-bottom: 1.8px;
  }
  .features-card li::before { content: "-"; position: absolute; left: 1px; }
  .features-card li.wrap-offgrid { width: 470px; }
  .features-card li.wrap-tax { width: 410px; }

  .product-render {
    position: absolute; left: 553px; top: 925px; width: 278px; height: 162px;
    border-radius: 6px;
    background:
      linear-gradient(180deg, #2e2f2e 0%, #2e2f2e 14%, #d9d4cb 24%, #ece7de 60%, #b39a76 88%, #3a3a3a 100%);
  }

  .closing {
    position: absolute; left: 70px; top: 1108px; width: 500px;
    color: var(--white); font-weight: 800; font-size: 14.6px; line-height: 19px;
  }
  .contact { position: absolute; left: 576px; top: 1113px; color: var(--white); }
  .contact .row { display: flex; align-items: center; gap: 8px; }
  .contact .phone { font-weight: 500; font-size: 18px; letter-spacing: 1.5px; }
  .contact .email { font-weight: 500; font-size: 12.4px; margin-top: 9px; }
</style>
</head>
<body>
<main class="flyer">
  <div class="hero-photo" role="img" aria-label="Photograph of a dark modern backyard office studio with glass walls and wooden double doors in a leafy garden"></div>

  <svg class="shapes" viewBox="0 0 874 1200" aria-hidden="true">
    <path d="M0,478 C150,560 320,600 520,578 C690,558 800,440 874,325 L874,640 L0,640 Z" fill="#f7960c"/>
    <path d="M160,585 C320,640 560,640 700,585 C780,553 840,510 874,470 L874,660 L160,660 Z" fill="#1f1f1f"/>
    <path d="M0,515 C180,605 380,630 560,618 C700,606 800,560 874,505 L874,1200 L0,1200 Z" fill="#ffffff"/>
    <path d="M0,1020 C80,975 170,950 300,945 L300,1200 L0,1200 Z" fill="#fbbf0b"/>
    <path d="M0,1065 C90,1010 190,985 320,985 L320,1200 L0,1200 Z" fill="#1f1f1f"/>
    <path d="M874,945 C800,955 720,975 600,995 L600,1200 L874,1200 Z" fill="#f7960c"/>
    <path d="M874,990 C790,1005 700,1030 560,1045 L560,1200 L874,1200 Z" fill="#1f1f1f"/>
    <rect x="0" y="1070" width="874" height="130" fill="#1f1f1f"/>
  </svg>

  <div class="brand-disc"></div>
  <div class="brand-mark"></div>
  <div class="brand-name">BRISK HOLLOW BUILDERS</div>

  <aside class="uses-card">
    <h3>PERFECT FOR :</h3>
    <ul>
      <li>Home Office</li>
      <li>Design Studio</li>
      <li>Artist Studio</li>
      <li>Home School Office</li>
      <li>Reading Room</li>
      <li>Craft Studio</li>
      <li>Drafting Room</li>
    </ul>
  </aside>

  <div class="delivery-badge">
    <div class="inner">
      <div class="lead">Delivered</div>
      <div class="big">100%</div>
      <div class="rest">Assembled<br>&amp; Ready<br>to Enjoy</div>
    </div>
  </div>

  <h1 class="headline">
    <span class="kicker">CEDARLANE</span>
    <span class="title">GARDEN<br>WORKROOM</span>
  </h1>

  <p class="intro">More and more people everyday are working from home and finding it difficult to disconnect from home activities in order to focus on their work. They are also finding it very expensive to add on to their existing house for a quiet place. Our archatectually stunning, Cedarlane Garden Workroom is the answer. The office studio measures 16' wide and 10' deep. 160 Square feet of space</p>

  <section class="features-card">
    <h3>Features :</h3>
    <ul>
      <li>Steel Framing. 40-60% lighter then wood, higher strength to weight ratio, resistant to mold and fire and steel is the most recycled material on earth!</li>
      <li>Spray foam insulation. Cool in the summer and warm in the winter.</li>
      <li>HVAC Mini Split with wireless remote control and thermostat.</li>
      <li class="wrap-offgrid">100% Off grid with enough solar and battery storage to run your entire office. No need to pay for an expensive electric installation.</li>
      <li>Flush fitting floor outlets to reduce wires.</li>
      <li>TV mount (Optional with pre-wired electric, HDMI, digital audio &amp; Cat 6)</li>
      <li>Windows are tempered glass custom made by Morvik Glazing.</li>
      <li class="wrap-tax">Solar qualifies for a 26% tax credit. This is not a write-off rather it is a direct reduction on your tax obligation.</li>
      <li>Thousands of dollars less than adding onto your home.</li>
      <li>Custom color, siding, features available.</li>
    </ul>
  </section>

  <div class="product-render" role="img" aria-label="Three-quarter view render of the garden workroom with dark siding and glass front"></div>

  <p class="closing">We ship nationwide from our factory in South Carolina.<br>Give us a call anytime to speak to a designer and<br>start your dream office today!</p>

  <div class="contact">
    <div class="row phone">
      <svg width="16" height="16" viewBox="0 0 24 24" aria-hidden="true"><path d="M6.6 10.8a15.1 15.1 0 0 0 6.6 6.6l2.2-2.2a1 1 0 0 1 1-.25 11.4 11.4 0 0 0 3.6.57 1 1 0 0 1 1 1V20a1 1 0 0 1-1 1A17 17 0 0 1 3 4a1 1 0 0 1 1-1h3.5a1 1 0 0 1 1 1c0 1.25.2 2.45.57 3.6a1 1 0 0 1-.25 1Z" fill="#fbbf0b"/></svg>
      <span>555-318-4027</span>
    </div>
    <div class="row email">
      <svg width="14" height="11" viewBox="0 0 24 18" aria-hidden="true"><rect width="24" height="18" rx="2" fill="#fbbf0b"/><path d="M1 2l11 8 11-8" stroke="#1f1f1f" stroke-width="2" fill="none"/></svg>
      <span>info@BriskHollowBuilders.example</span>
    </div>
  </div>
</main>
</body>
</html>
```